Start-up needs a Web Design

We need a web design for a new Cleantech start-up based in California called "Ferrovane".

Background info on our company:

Our company is active in the area of wastewater treatment. We have a patent-pending treatment system to clean the wastewater that is collected by vacuum trucks from septic tanks. The cleaned water can be re-used.

Our clients can save up to 90% of the wastewater discharge fees by using our system instead of just dumping it.

The two founders of the company have successfully launched other Cleantech and Medtech startups before.

We are offering our services in the United States, Canada, Mexico, and the whole of Southern America.
Updates

Dear Designers for Ferrovane,

I have just updated the brief for the website of Ferrovane.

The main change to the brief is that the main graphic / photo of the website should not be "How it works", but a photo of Truck / containter.

All the best, Martin

Target Market(s)

n.a.

Industry/Entity Type

It Company

Requirements
Must have
• non
Nice to have
• non
Should not have
• n.a.

```html
<!DOCTYPE html>
<html lang="en">
<head>
<meta charset="utf-8">
<title>Ferrovane — Wastewater Treatment</title>
<link rel="stylesheet" href="https://fonts.googleapis.com/css2?family=Arimo:wght@400;700&family=Rokkitt:wght@400;700&family=Tinos:wght@400;700&display=swap">
<style>
:root{
  --sky:#1aa3ea;
  --sky-deep:#0a83d4;
  --navy:#12305d;
  --ink:#1b1b1b;
  --tab-blue:#2d8fd1;
  --link-blue:#1f7fe0;
  --brand-blue:#0a2bb2;
  --hero-blue:#4f88dc;
  --panel-edge:#c9d3de;
  --nav-dark:#151515;
  --white:#ffffff;
}
*{box-sizing:border-box;margin:0;padding:0}
html,body{width:922px;height:1200px;overflow:hidden;background:var(--white)}
body{position:relative;font-family:"Arimo",Arial,sans-serif;color:var(--ink)}

.topbar{position:absolute;left:0;top:0;width:922px;height:51px;
  background:linear-gradient(#2cb4f2,var(--sky-deep));color:var(--white)}
.topbar .call{position:absolute;left:16px;top:14px;font-family:"Tinos",serif;font-size:17px}
.topbar .call strong{font-family:"Arimo",sans-serif;font-size:19px;letter-spacing:.5px;color:#0b0b0b;margin-left:4px}
.topbar .subscribe{position:absolute;left:490px;top:14px;font-family:"Tinos",serif;font-size:17px}
.topbar .email{position:absolute;left:656px;top:14px;width:167px;height:22px;border:1px solid #9aa;background:#ececec;
  font-family:"Arimo",sans-serif;font-size:10px;color:#8b8b8b;padding:5px 8px}
.topbar .submit{position:absolute;left:829px;top:14px;width:70px;height:22px;background:#111;color:var(--white);
  font-size:13px;text-align:center;line-height:22px;border:1px solid #555}

.masthead{position:absolute;left:0;top:51px;width:922px;height:104px;
  background:linear-gradient(#d7ecfb,#f3f9fe 55%,#fff)}
.logo{position:absolute;left:20px;top:24px;display:flex;align-items:center;gap:10px}
.logo .mark{width:50px;height:50px;background:var(--navy);border-radius:50%}
.logo .name{font-family:"Arimo",sans-serif;font-weight:700;font-size:44px;color:#0f0f0f;letter-spacing:-.5px}

.mainnav{position:absolute;left:10px;top:156px;width:902px;height:45px;display:flex;
  background:linear-gradient(#4a4a4a,#1c1c1c 50%,var(--nav-dark))}
.mainnav a{flex:auto;color:var(--white);text-decoration:none;font-size:15px;line-height:45px;text-align:center;
  border-right:1px solid #3c3c3c}
.mainnav a:last-child{border-right:0}
.mainnav a.active{color:#36b2f3;text-align:left;padding-left:10px;flex:0 0 103px}

.hero{position:absolute;left:10px;top:206px;width:902px;height:295px;border:1px solid #e2e2e2;padding:3px 6px}
.hero .stage{position:absolute;left:7px;top:3px;width:888px;height:287px;
  background:linear-gradient(160deg,#5d97e6,var(--hero-blue) 60%,#3f77cc)}
.hero .welcome{position:absolute;left:16px;top:33px;width:440px;padding-bottom:6px;border-bottom:1px solid #c3d8f3;
  font-family:"Rokkitt",serif;font-size:17px;color:var(--white)}
.hero .welcome b{font-size:35px;color:var(--brand-blue);margin-left:6px;letter-spacing:.5px}
.hero .intro{position:absolute;left:16px;top:79px;width:430px;font-family:"Tinos",serif;font-size:16.5px;line-height:21px;color:var(--white)}
.hero .more{position:absolute;left:16px;top:170px;width:156px;height:36px;border-radius:18px;
  background:linear-gradient(#2a4f85,#0b1d3b);color:var(--white);font-family:"Tinos",serif;font-size:17px;line-height:36px;padding-left:24px}
.hero .more::after{content:" ›";font-size:15px}
.hero .truck-photo{position:absolute;left:510px;top:30px;width:370px;height:240px;border-radius:6px;
  background:linear-gradient(180deg,#c9daf1,#eef1f5 45%,#8c949c)}

.section-title{position:absolute;font-family:"Rokkitt",serif;font-weight:700;font-size:23px;color:var(--ink)}
.how-title{left:14px;top:514px}

.tab{position:absolute;top:547px;height:32px;border-radius:8px 8px 0 0;font-family:"Tinos",serif;font-size:14px;text-align:center;line-height:32px}
.tab.old{left:37px;width:152px;background:var(--navy);color:var(--white)}
.tab.new{left:191px;width:151px;background:var(--tab-blue);color:#0b1d3b;top:549px;height:30px;line-height:30px}

.process{position:absolute;left:12px;top:578px;width:898px;height:156px;background:var(--navy);
  border:3px solid var(--panel-edge);border-radius:12px}
.step{position:absolute;top:17px;width:233px;height:117px;border-radius:14px;border:2px solid var(--white)}
.step.factory{left:18px;background:linear-gradient(#d9ecfa,#f3a46a 70%,#e8eef2)}
.step.truck{left:311px;background:var(--white)}
.step.truck svg{position:absolute;left:40px;top:10px}
.step.plant{left:645px;background:linear-gradient(#c8d3d9,#7e8b86 60%,#5d6b5f)}
.flow-label{position:absolute;top:67px;height:25px;background:#1d1d1d;color:var(--white);font-weight:700;font-size:13px;
  line-height:25px;padding-left:12px;clip-path:polygon(0 0,92% 0,100% 50%,92% 100%,0 100%)}
.flow-label.waste{left:228px;width:112px}
.flow-label.dump{left:523px;width:152px}

.facts{position:absolute;left:32px;top:742px;list-style:none;font-family:"Tinos",serif;font-size:16.5px;color:var(--link-blue)}
.facts li{position:relative;padding-left:16px;height:25px}
.facts li::before{content:"";position:absolute;left:0;top:6px;border-left:6px solid #111;border-top:4px solid transparent;border-bottom:4px solid transparent}

.about-title{left:22px;top:832px;width:584px;padding-bottom:2px;border-bottom:1px dashed #333}
.about-copy{position:absolute;left:21px;top:874px;width:585px;font-size:10.7px;line-height:16px;color:#222}
.about-copy p+p{margin-top:16px}
.about-photo{position:absolute;left:630px;top:865px;width:282px;height:220px;border:1px solid #d2d2d2;border-radius:14px;padding:6px}
.about-photo div{width:100%;height:100%;border-radius:10px;background:linear-gradient(#f6f6f6,#d8dadc 50%,#6e6e6e)}

.footer{position:absolute;left:0;top:1146px;width:922px;height:54px;background:linear-gradient(#4a4a4a,#111);
  color:var(--white);font-size:10px;text-align:center;line-height:54px}
.footer span{margin:0 8px}
</style>
</head>
<body>

<header class="topbar">
  <div class="call">CALL US : <strong>555 0142 0199</strong></div>
  <div class="subscribe">Subscribe Newsletter</div>
  <div class="email">Type your email id</div>
  <div class="submit">Submit</div>
</header>

<div class="masthead">
  <div class="logo"><span class="mark"></span><span class="name">Ferrovane</span></div>
</div>

<nav class="mainnav">
  <a class="active" href="#">Home</a>
  <a href="#">About Us</a>
  <a href="#">Our Service</a>
  <a href="#">How It Works</a>
  <a href="#">Clients</a>
  <a href="#">Testimonial</a>
  <a href="#">Contact Us</a>
</nav>

<section class="hero">
  <div class="stage">
    <h1 class="welcome">WELCOME TO<b>FERROVANE</b></h1>
    <p class="intro">We have spent many years treating wastewater from totally different industries. From this experience we know the best and easiest ways to treat wastewater.</p>
    <div class="more">Read More</div>
    <div class="truck-photo" role="img" aria-label="Photo of a white company semi-truck with container under a blue sky"></div>
  </div>
</section>

<h2 class="section-title how-title">How It Works</h2>
<div class="tab old">Old Process</div>
<div class="tab new">Ferrovane Process</div>
<div class="process">
  <div class="step factory" role="img" aria-label="Illustration of a factory producing wastewater"></div>
  <div class="step truck">
    <svg width="150" height="95" viewBox="0 0 150 95" aria-label="Vacuum truck icon">
      <path d="M6 6h88v62H6z M98 22h24l22 24v22H98z" fill="#111"/>
      <path d="M104 28h16l14 16h-30z" fill="#fff"/>
      <circle cx="32" cy="74" r="15" fill="#111"/><circle cx="32" cy="74" r="7" fill="#fff"/>
      <circle cx="118" cy="74" r="15" fill="#111"/><circle cx="118" cy="74" r="7" fill="#fff"/>
    </svg>
  </div>
  <div class="step plant" role="img" aria-label="Photo of a municipal wastewater treatment plant"></div>
  <div class="flow-label waste">Wastewater</div>
  <div class="flow-label dump">Dump &amp; Pay (Old)</div>
</div>

<ul class="facts">
  <li>Dump &amp; Pay was old process and too much expensive</li>
  <li>Ferrovane offers to clean the solution and reuse it in low cost</li>
</ul>

<h2 class="section-title about-title">About Us</h2>
<div class="about-copy">
  <p>Lorem ipsum dolor sit amet, consectetur adipiscing elit. Pellentesque magna massa, tincidunt in lacinia non, consectetur posuere purus. Donec tempor sem vitae purus tincidunt egestas. Cum sociis natoque penatibus et magnis dis parturient montes, nascetur ridiculus mus. Phasellus vel sem eu est porttitor iaculis. Sed elit neque, aliquam posuere congue sed, cursus sed enim. Suspendisse potenti. Quisque nulla mauris, mattis vitae pellentesque quis, faucibus in metus. In hac habitasse platea dictumst. Mauris ut nibh eu diam pretium lacinia. Donec vel iaculis ipsum. Sed a leo non nulla faucibus adipiscing vel non turpis. Suspendisse id imperdiet lectus. Donec vel velit ut lacus porttitor lobortis vel non enim. Aenean aliquet auctor lacus, non hendrerit mauris porttitor ac.</p>
  <p>Donec tempor sem vitae purus tincidunt egestas. Cum sociis natoque penatibus et magnis dis parturient montes, nascetur ridiculus mus. Phasellus vel sem eu est porttitor iaculis. Sed elit neque, aliquam posuere congue sed, cursus sed enim. Suspendisse potenti. Quisque nulla mauris, mattis vitae pellentesque quis, faucibus in metus. In hac habitasse platea dictumst. Mauris ut nibh eu diam pretium lacinia. Donec vel iaculis ipsum. Sed a leo non nulla faucibus adipiscing vel non turpis.</p>
</div>
<div class="about-photo"><div role="img" aria-label="Photo of a white vacuum tank truck seen from the rear"></div></div>

<footer class="footer">© 2011 All Rights Reserved<span>|</span>Privacy Policy<span>|</span>Terms &amp; Conditions</footer>

</body>
</html>
```